PALS postcard design

We need a design for a non profit organization associated with an animal shelter called PALS of NHRPC. NHRPC stands for Northbrook Hollow Regional Pet Center. This 501c3 group provides assistance to the community in the form of training, consultation, financial assistance, education and more. Our goal is to provide options to people in need to help them keep their pets rather than surrender them to the shelter. We have a logo already but we need something for people to take away and to use as a handout. Need to include phone numbers and website, which I will provide.

Target Market(s)

general public who have pets

Industry/Entity Type

Non Profit

Font styles to use
Sans Serif
Other font styles liked:
• designer can choose others

Requirements
Must have
• The logo must be fairly large. Colors should be bright and eye-pleasing. Like colors that match the logo. Easy to read fonts. Pics of animals are OK but no pics with people. Not too much text, short and to the point.
Nice to have
• not sure
Should not have
• No pics with people. Not black and white. Not too much text.

```html
<!DOCTYPE html>
<html lang="en">
<head>
<meta charset="utf-8">
<title>PALS of NHRPC Postcard</title>
<link rel="stylesheet" href="https://fonts.googleapis.com/css2?family=Bebas+Neue&family=Roboto+Condensed:wght@400;700&display=swap">
<style>
  :root {
    --sky: #2bc0e4;
    --sun: #f7ec1c;
    --coral: #ef3e36;
    --white: #ffffff;
    --pup-tone: #8a8f6a;
    --cat-tone: #8c7662;
  }
  * { margin: 0; padding: 0; box-sizing: border-box; }
  html, body { width: 1200px; height: 662px; overflow: hidden; background: var(--white); }
  .postcard {
    position: relative;
    width: 1200px;
    height: 662px;
    background: var(--white);
    font-family: "Roboto Condensed", "Arial Narrow", sans-serif;
    font-weight: 700;
  }
  .intro {
    position: absolute; left: 0; top: 0;
    width: 1200px; height: 338px;
    background: var(--sky);
  }
  .brand {
    position: absolute; left: 50px; top: 50px;
    width: 300px; height: 250px;
    display: flex; flex-direction: column; align-items: center; justify-content: center; gap: 26px;
  }
  .brand-dot {
    width: 120px; height: 120px; border-radius: 50%;
    background: var(--coral);
  }
  .brand-name {
    font-family: "Bebas Neue", "Arial Narrow", sans-serif;
    font-weight: 400;
    font-size: 46px;
    line-height: 46px;
    color: var(--coral);
    letter-spacing: 1px;
    white-space: nowrap;
  }
  .headline {
    position: absolute; left: 403px; top: 28px;
    width: 770px;
    font-family: "Bebas Neue", "Arial Narrow", sans-serif;
    font-weight: 400;
    font-size: 57px;
    line-height: 57px;
    color: var(--white);
    text-transform: uppercase;
    white-space: nowrap;
  }
  .headline .accent { color: var(--sun); }
  .mission {
    position: absolute; left: 403px; top: 154px;
    width: 755px;
    font-size: 16px;
    line-height: 25.7px;
    color: var(--white);
    text-align: justify;
  }
  .photo {
    position: absolute; top: 342px; height: 249px;
  }
  .photo-dog { left: 0; width: 362px; background: linear-gradient(160deg, #c9cbb0, var(--pup-tone) 60%, #3e5a2a); }
  .photo-cat { left: 366px; width: 361px; background: linear-gradient(160deg, #5a4838, var(--cat-tone) 55%, #d8c8b8); }
  .help {
    position: absolute; left: 731px; top: 342px;
    width: 469px; height: 249px;
    background: var(--coral);
    color: var(--white);
    padding: 17px 22px 0 25px;
  }
  .help-title {
    font-family: "Bebas Neue", "Arial Narrow", sans-serif;
    font-weight: 400;
    font-size: 36px;
    line-height: 38px;
    color: var(--sun);
    text-transform: uppercase;
    margin-bottom: 10px;
  }
  .help-item {
    font-size: 14.6px;
    line-height: 19.5px;
    margin-bottom: 11px;
  }
  .help-item strong { font-size: 17px; }
  .help-web-label {
    margin-top: 20px;
    font-size: 14.6px;
    line-height: 18px;
  }
  .help-web {
    font-size: 24px;
    line-height: 30px;
    color: var(--sun);
    padding-left: 3px;
  }
  .callout {
    position: absolute; left: 0; top: 595px;
    width: 1200px; height: 67px;
    background: var(--sky);
    display: flex; align-items: center; justify-content: center;
    font-family: "Bebas Neue", "Arial Narrow", sans-serif;
    font-weight: 400;
    font-size: 37px;
    line-height: 40px;
    padding-top: 4px;
    color: var(--sun);
    text-transform: uppercase;
    white-space: nowrap;
  }
</style>
</head>
<body>
<main class="postcard">
  <section class="intro">
    <div class="brand">
      <span class="brand-dot" aria-hidden="true"></span>
      <span class="brand-name">PALS of NHRPC</span>
    </div>
    <h1 class="headline">Supporting the shelter in their<br>goal to create <span class="accent">a no-kill community</span></h1>
    <p class="mission">Pals of Northbrook Hollow Regional Pet Center is an integral part of Northbrook’s lifesaving mission. We provide behavioral enrichment programs for adopted dogs and are in the process of creating an assistance program for families who are experiencing financial troubles due to animal related expenses such as pet deposits or medical costs. We will also offer free training consults, both in the home and at the shelter, for those who need it. Our focus is to create second chances for families who think their only solution is surrendering a pet to a shelter or simply abandoning them.</p>
  </section>

  <div class="photo photo-dog" role="img" aria-label="Photo of a happy small white terrier standing on grass"></div>
  <div class="photo photo-cat" role="img" aria-label="Photo of a tabby and white cat lying down, looking ahead"></div>

  <section class="help">
    <h2 class="help-title">How can you help?</h2>
    <p class="help-item"><strong>Volunteers</strong> are needed for fundraising, program and volunteer committees. Plus hands on work at the shelter!</p>
    <p class="help-item"><strong>Donations</strong> will support our continuing education, community outreach and intervention programs.</p>
    <p class="help-web-label">Visit Our Website For More Information</p>
    <p class="help-web">www.palsofnhrpc.org</p>
  </section>

  <footer class="callout">If you need assistance please call 555-014-0392</footer>
</main>
</body>
</html>
```